Design Vextora Ads for PanTally

Market Overview:

The food safety management system market is highly competitive, with many systems offering comprehensive features that go beyond basic food logging. These systems often include functionalities such as workplace safety, staff management, and advanced food labelling.

PanTally Differentiation:

PanTally stands out in this crowded market due to its simplicity and affordability. Unlike many competitors, PanTally focuses exclusively on essential food safety tasks, making it an ideal solution for small food-based businesses. These are businesses that typically rely on pen and paper for minimal recording of temperatures, food logs, delivery logs, and simple task management.

Target Audience:

PanTally is designed for small food-based businesses that need an efficient, cost-effective solution for basic food safety and logging tasks. These businesses are not looking for comprehensive systems that include workplace safety, staff management, or advanced food labelling. Instead, they need a straightforward tool to transition from manual record-keeping to a digital solution without incurring high costs.

Key Benefits:

Cost-Effective: PanTally is significantly cheaper than many competitors because it focuses solely on essential food safety functions.

User-Friendly: The simplicity of PanTally makes it easy for small businesses to implement and use without extensive training or support.

Targeted Solution: By concentrating on basic food safety tasks, PanTally provides exactly what small food-based businesses need, avoiding the complexity and expense of more comprehensive systems.

This focus on affordability, simplicity, and targeted functionality makes PanTally the perfect solution for small food businesses looking to improve their food safety management without the added cost and complexity of larger systems.
We want some Vextora Display Ads.

Vextora Display Ad Sizes:
300x250
336x280
300x600
728x90
160x600
Ad Title: The Restaurant Food Safety App

Brand: PanTally

Main Line:
The Restaurant Food Safety App

Key Points:
Streamline HACCP Audits
Eliminate Paperwork

Call to Action (CTA):
Start Your Free Trial Today

Visual Elements:
PanTally Logo prominently displayed
Clean, modern design emphasising simplicity and efficiency
Visuals of the app in use, highlighting key features like audit streamlining and paperless operation

Tone:
Professional, efficient, and user-friendly

Target Audience:
Restaurant owners and managers
Food safety compliance officers

Objective:
Highlight the app's capability to streamline food safety audits and reduce paperwork
Encourage potential users to start a free trial

Ad Title: Ditch Paperwork, Streamline Food Safety

Brand: PanTally

Main Line:
Ditch Paperwork, Streamline Food Safety

Key Points:
Easy to Use
HACCP Approved

Call to Action (CTA):

Visual Elements:
Clean, modern design emphasising ease of use and HACCP approval
Visuals showcasing the simplicity and effectiveness of the app

Tone:
Professional, straightforward, and efficient

Target Audience:

Objective:
Highlight the app's user-friendliness and HACCP approval

TIP: Submit one design and if you are selected you can then design the other ratios of ads keeping the exact same design.

Target Market(s)

Restaurants & Cafe Owners

Industry/Entity Type

Hospitality

Requirements
Must have
• PanTally Logo Main copy line and CTA
Nice to have
• Main copy Line I but in brief and the key points
Should not have
• Ugly design

```html
<!DOCTYPE html>
<html lang="en">
<head>
<meta charset="utf-8">
<title>PanTally Display Ads</title>
<link rel="stylesheet" href="https://fonts.googleapis.com/css2?family=Montserrat:wght@700&family=Oswald:wght@500&family=Roboto:wght@700&display=swap">
<style>
  :root {
    --navy: #0d1626;
    --teal: #38b9c7;
    --lime: #c9dc2c;
    --white: #ffffff;
    --ink: #111a24;
  }
  * { margin: 0; padding: 0; box-sizing: border-box; }
  html, body { width: 1200px; height: 1200px; overflow: hidden; background: var(--white); }
  .canvas { position: relative; width: 1200px; height: 1200px; }

  .ad { position: absolute; background: var(--navy); overflow: hidden; }
  .ad > * { position: absolute; }
  .ad-backdrop { left: 0; top: 0; width: 100%; height: 100%; }

  .photo {
    background: linear-gradient(180deg, #6b4a36 0%, #b88a70 22%, #f2f2f2 42%, #9a9ca2 70%, #7e8087 100%);
    border-radius: 40% 40% 0 0;
  }

  .brand { display: flex; align-items: center; gap: 6px; }
  .brand-name { font-family: "Montserrat", sans-serif; font-weight: 700; color: var(--white); letter-spacing: -0.3px; }
  .brand-seal { border-radius: 50%; background: var(--white); opacity: 0.9; flex: none; }

  .headline { font-family: "Montserrat", sans-serif; font-weight: 700; color: var(--white); }
  .headline .accent { color: var(--teal); }
  .headline span { display: block; }

  .points { list-style: none; font-family: "Oswald", sans-serif; font-weight: 500; color: var(--white); text-transform: uppercase; letter-spacing: -0.2px; }
  .points li { display: flex; align-items: center; }
  .points li::before { content: ""; border-radius: 50%; background: var(--lime); flex: none; }

  .cta {
    display: flex; align-items: center; justify-content: center; gap: 5px;
    background: var(--lime); color: var(--ink);
    font-family: "Roboto", sans-serif; font-weight: 700; border-radius: 5px; white-space: nowrap;
  }
  .cta svg { flex: none; }

  /* 300 x 250 */
  .ad-medium { left: 19px; top: 250px; width: 283px; height: 235px; }
  .ad-medium .brand { left: 19px; top: 20px; }
  .ad-medium .brand-name { font-size: 19px; }
  .ad-medium .brand-seal { width: 26px; height: 26px; }
  .ad-medium .headline { left: 26px; top: 66px; font-size: 18.5px; line-height: 21px; }
  .ad-medium .points { left: 26px; top: 157px; font-size: 12px; line-height: 17px; }
  .ad-medium .points li::before { width: 5px; height: 5px; margin-right: 9px; }
  .ad-medium .photo { left: 160px; top: 22px; width: 122px; height: 213px; }
  .ad-medium .cta { left: 32px; top: 202px; width: 135px; height: 21px; font-size: 9px; }

  /* 336 x 280 */
  .ad-large { left: 314px; top: 250px; width: 317px; height: 264px; }
  .ad-large .brand { left: 19px; top: 24px; }
  .ad-large .brand-name { font-size: 22px; }
  .ad-large .brand-seal { width: 31px; height: 31px; }
  .ad-large .headline { left: 29px; top: 78px; font-size: 21px; line-height: 23px; }
  .ad-large .points { left: 29px; top: 176px; font-size: 13.5px; line-height: 19px; }
  .ad-large .points li::before { width: 6px; height: 6px; margin-right: 10px; }
  .ad-large .photo { left: 170px; top: 12px; width: 147px; height: 252px; }
  .ad-large .cta { left: 30px; top: 224px; width: 152px; height: 24px; font-size: 10.5px; }

  /* 160 x 600 */
  .ad-skyscraper { left: 643px; top: 250px; width: 151px; height: 565px; }
  .ad-skyscraper .brand { left: 9px; top: 32px; gap: 4px; }
  .ad-skyscraper .brand-name { font-size: 18px; }
  .ad-skyscraper .brand-seal { width: 28px; height: 28px; }
  .ad-skyscraper .headline { left: 13px; top: 82px; font-size: 18.5px; line-height: 21.5px; }
  .ad-skyscraper .points { left: 13px; top: 180px; font-size: 13.5px; line-height: 21px; }
  .ad-skyscraper .points li::before { width: 6px; height: 6px; margin-right: 10px; }
  .ad-skyscraper .photo { left: 0; top: 268px; width: 151px; height: 297px; }
  .ad-skyscraper .cta { left: 7px; top: 498px; width: 138px; height: 22px; font-size: 9px; }

  /* 300 x 600 */
  .ad-halfpage { left: 802px; top: 250px; width: 283px; height: 565px; }
  .ad-halfpage .brand { left: 37px; top: 26px; gap: 10px; }
  .ad-halfpage .brand-name { font-size: 30px; }
  .ad-halfpage .brand-seal { width: 44px; height: 44px; }
  .ad-halfpage .headline { left: 43px; top: 95px; font-size: 28px; line-height: 30.5px; }
  .ad-halfpage .points { left: 43px; top: 233px; font-size: 15px; display: flex; gap: 14px; }
  .ad-halfpage .points li::before { width: 6px; height: 6px; margin-right: 10px; }
  .ad-halfpage .photo { left: 40px; top: 258px; width: 236px; height: 307px; }
  .ad-halfpage .cta { left: 63px; top: 488px; width: 195px; height: 31px; font-size: 13px; }

  /* 728 x 90 */
  .ad-leaderboard { left: 397px; top: 844px; width: 686px; height: 86px; }
  .ad-leaderboard .brand { left: 17px; top: 26px; gap: 10px; }
  .ad-leaderboard .brand-name { font-size: 22px; }
  .ad-leaderboard .brand-seal { width: 31px; height: 31px; }
  .ad-leaderboard .headline { left: 185px; top: 11px; font-size: 18px; line-height: 22px; }
  .ad-leaderboard .headline span { display: inline; }
  .ad-leaderboard .headline .line { display: block; }
  .ad-leaderboard .points { left: 185px; top: 59px; font-size: 13.5px; display: flex; gap: 14px; }
  .ad-leaderboard .points li::before { width: 6px; height: 6px; margin-right: 10px; }
  .ad-leaderboard .photo { left: 406px; top: 2px; width: 104px; height: 84px; }
  .ad-leaderboard .cta { left: 508px; top: 37px; width: 162px; height: 26px; font-size: 11px; }
</style>
</head>
<body>
<main class="canvas">

  <section class="ad ad-medium" aria-label="PanTally 300 by 250 ad">
    <svg class="ad-backdrop" viewBox="0 0 283 235" aria-hidden="true">
      <circle cx="330" cy="120" r="162" fill="var(--teal)"/>
      <circle cx="345" cy="130" r="182" fill="none" stroke="var(--navy)" stroke-width="2.5"/>
    </svg>
    <div class="photo" role="img" aria-label="Smiling chef in white t-shirt and striped apron with arms crossed"></div>
    <div class="brand"><span class="brand-name">PanTally</span><span class="brand-seal"></span></div>
    <h2 class="headline"><span>Ditch</span><span class="accent">Paperwork</span><span>Streamline</span><span class="accent">Food Safety</span></h2>
    <ul class="points"><li>Easy to use</li><li>HACCP approved</li></ul>
    <a class="cta">Start Your Free Trial Today <svg width="6" height="9" viewBox="0 0 6 9"><path d="M1 1l3.5 3.5L1 8" fill="none" stroke="var(--ink)" stroke-width="1.8"/></svg></a>
  </section>

  <section class="ad ad-large" aria-label="PanTally 336 by 280 ad">
    <svg class="ad-backdrop" viewBox="0 0 317 264" aria-hidden="true">
      <circle cx="375" cy="135" r="185" fill="var(--teal)"/>
      <circle cx="390" cy="145" r="205" fill="none" stroke="var(--navy)" stroke-width="2.5"/>
    </svg>
    <div class="photo" role="img" aria-label="Smiling chef in white t-shirt and striped apron with arms crossed"></div>
    <div class="brand"><span class="brand-name">PanTally</span><span class="brand-seal"></span></div>
    <h2 class="headline"><span>Ditch</span><span class="accent">Paperwork</span><span>Streamline</span><span class="accent">Food Safety</span></h2>
    <ul class="points"><li>Easy to use</li><li>HACCP approved</li></ul>
    <a class="cta">Start Your Free Trial Today <svg width="7" height="10" viewBox="0 0 7 10"><path d="M1.5 1l3.5 4-3.5 4" fill="none" stroke="var(--ink)" stroke-width="2"/></svg></a>
  </section>

  <section class="ad ad-skyscraper" aria-label="PanTally 160 by 600 ad">
    <svg class="ad-backdrop" viewBox="0 0 151 565" aria-hidden="true">
      <circle cx="175" cy="570" r="300" fill="var(--teal)"/>
      <circle cx="190" cy="580" r="310" fill="none" stroke="var(--navy)" stroke-width="2.5"/>
    </svg>
    <div class="photo" role="img" aria-label="Smiling chef in white t-shirt and striped apron with arms crossed"></div>
    <div class="brand"><span class="brand-name">PanTally</span><span class="brand-seal"></span></div>
    <h2 class="headline"><span>Ditch</span><span class="accent">Paperwork</span><span>Streamline</span><span class="accent">Food Safety</span></h2>
    <ul class="points"><li>Easy to use</li><li>HACCP approved</li></ul>
    <a class="cta">Start Your Free Trial Today <svg width="6" height="9" viewBox="0 0 6 9"><path d="M1 1l3.5 3.5L1 8" fill="none" stroke="var(--ink)" stroke-width="1.8"/></svg></a>
  </section>

  <section class="ad ad-halfpage" aria-label="PanTally 300 by 600 ad">
    <svg class="ad-backdrop" viewBox="0 0 283 565" aria-hidden="true">
      <circle cx="142" cy="770" r="400" fill="var(--teal)"/>
      <circle cx="142" cy="790" r="415" fill="none" stroke="var(--navy)" stroke-width="2.5"/>
    </svg>
    <div class="photo" role="img" aria-label="Smiling chef in white t-shirt and striped apron with arms crossed"></div>
    <div class="brand"><span class="brand-name">PanTally</span><span class="brand-seal"></span></div>
    <h2 class="headline"><span>Ditch</span><span class="accent">Paperwork</span><span>Streamline</span><span class="accent">Food Safety</span></h2>
    <ul class="points"><li>Easy to use</li><li>HACCP approved</li></ul>
    <a class="cta">Start Your Free Trial Today <svg width="8" height="12" viewBox="0 0 8 12"><path d="M1.5 1.5l4.5 4.5-4.5 4.5" fill="none" stroke="var(--ink)" stroke-width="2.2"/></svg></a>
  </section>

  <section class="ad ad-leaderboard" aria-label="PanTally 728 by 90 ad">
    <svg class="ad-backdrop" viewBox="0 0 686 86" aria-hidden="true">
      <circle cx="800" cy="43" r="240" fill="var(--teal)"/>
      <line x1="601" y1="0" x2="601" y2="86" stroke="var(--navy)" stroke-width="2.5"/>
      <circle cx="760" cy="43" r="90" fill="none" stroke="var(--navy)" stroke-width="2.5"/>
    </svg>
    <div class="photo" role="img" aria-label="Smiling chef in white t-shirt and striped apron"></div>
    <div class="brand"><span class="brand-name">PanTally</span><span class="brand-seal"></span></div>
    <h2 class="headline"><span class="line"><span>Ditch </span><span class="accent">Paperwork</span></span><span class="line"><span>Streamline </span><span class="accent">Food Safety</span></span></h2>
    <ul class="points"><li>Easy to use</li><li>HACCP approved</li></ul>
    <a class="cta">Start Your Free Trial Today <svg width="7" height="10" viewBox="0 0 7 10"><path d="M1.5 1l3.5 4-3.5 4" fill="none" stroke="var(--ink)" stroke-width="2"/></svg></a>
  </section>

</main>
</body>
</html>
```